Plumbing & Heating company

A leaflet containing -

Company name - Brackenfold Plumbing Solutions
logo
Mobile number - 07700 914226
Landline - 01632 870512
Email - Info@brackenfoldplumbing.example.co.uk
website - Brackenfold-plumbing.example.co.uk
Social media logos - pixgram, Chatterly

services we offer

- Boiler replacements (free quote)
- General plumbing & heating
- Tap replacements
- 1st & 2nd
- New builds & Extensions
- Cylinder replcemets

```html
<!DOCTYPE html>
<html lang="en">
<head>
<meta charset="UTF-8">
<title>Brackenfold Plumbing Solutions – Leaflet</title>
<link rel="stylesheet" href="https://fonts.googleapis.com/css2?family=Antonio:wght@700&family=Outfit:wght@400;800&display=swap">
<style>
  :root {
    --bg: #1c1c1c;
    --orange: #f39a24;
    --flame-light: #f2b247;
    --flame-deep: #e8583e;
    --blue: #3a8ccc;
    --blue-deep: #2b64a4;
    --white: #ffffff;
    --photo-light: #dedad3;
    --photo-warm: #c39a6c;
    --photo-dark: #3a3633;
  }
  * { margin: 0; padding: 0; box-sizing: border-box; }
  html, body { width: 825px; height: 1200px; overflow: hidden; background: var(--bg); }
  .leaflet {
    position: relative; width: 825px; height: 1200px; overflow: hidden;
    background: var(--bg); font-family: "Outfit", sans-serif; color: var(--orange);
  }
  .artwork { position: absolute; inset: 0; }
  .brand {
    position: absolute; left: 60px; top: 150px; width: 510px; text-align: center;
    font-family: "Outfit", sans-serif; font-weight: 800; color: var(--orange); line-height: 1;
  }
  .brand-main { display: block; font-size: 66px; letter-spacing: 1px; }
  .brand-sub { display: block; font-size: 24px; letter-spacing: 4px; margin-top: 20px; }
  .services-heading { position: absolute; left: 0; top: 324px; display: flex; align-items: center; }
  .services-heading h2 {
    font-family: "Antonio", sans-serif; font-weight: 700; font-size: 48px;
    color: var(--orange); margin-left: 10px; line-height: 1; text-transform: uppercase;
  }
  .band { display: block; background: var(--blue); height: 12px; flex: none; }
  .service-list { position: absolute; left: 0; top: 412px; list-style: none; }
  .service-list li {
    display: flex; align-items: center; height: 47px;
    font-size: 24.5px; font-weight: 400; color: var(--orange);
  }
  .service-list .band { width: 110px; margin-right: 12px; }
  .call { position: absolute; left: 44px; top: 756px; }
  .call-icon { position: absolute; left: 0; top: 16px; }
  .call-title, .call-number {
    position: absolute; white-space: nowrap;
    font-family: "Antonio", sans-serif; font-weight: 700; font-size: 62px; line-height: 1;
  }
  .call-title { left: 53px; top: 0; color: var(--orange); }
  .call-number { left: 104px; top: 62px; color: var(--white); }
  .contacts { position: absolute; left: 43px; top: 930px; list-style: none; }
  .contacts li {
    display: flex; align-items: center; height: 49px;
    font-size: 19px; color: var(--white);
  }
  .contacts li svg { margin-right: 12px; flex: none; }
  .social {
    position: absolute; left: 148px; top: 1100px; display: flex; gap: 14px;
    font-size: 13px; color: var(--white);
  }
  .social span { display: flex; align-items: center; gap: 5px; }
  .social i { display: inline-block; width: 24px; height: 24px; border-radius: 50%; background: var(--white); }
  .footer-name { position: absolute; left: 79px; top: 1141px; font-size: 15px; color: var(--white); }
</style>
</head>
<body>
<div class="leaflet">
  <svg class="artwork" width="825" height="1200" viewBox="0 0 825 1200">
    <defs>
      <linearGradient id="artGrad" x1="0" y1="0" x2="0" y2="1">
        <stop offset="0" stop-color="var(--flame-deep)"/>
        <stop offset="0.3" stop-color="var(--flame-light)"/>
        <stop offset="0.45" stop-color="var(--blue-deep)"/>
        <stop offset="1" stop-color="var(--blue)"/>
      </linearGradient>
    </defs>
    <path role="img" aria-label="Illustration: orange flame behind a large blue water drop"
      fill="url(#artGrad)" d="M590 96 H825 V1200 H470 V560 H590 Z"/>
    <rect role="img" aria-label="Photo: boiler beside a hot water cylinder with copper pipework"
      x="580" y="485" width="226" height="325" rx="18" fill="var(--photo-light)"/>
    <rect role="img" aria-label="Photo: boiler installation with copper pipes on a plywood wall"
      x="488" y="740" width="160" height="265" rx="18" fill="var(--photo-warm)"/>
    <rect role="img" aria-label="Photo: copper pipework manifold on a dark wall"
      x="604" y="890" width="202" height="283" rx="18" fill="var(--photo-dark)"/>
  </svg>

  <h1 class="brand">
    <span class="brand-main">BRACKENFOLD</span>
    <span class="brand-sub">PLUMBING SOLUTIONS</span>
  </h1>

  <div class="services-heading">
    <span class="band" style="width:247px"></span>
    <h2>Services We Offer</h2>
  </div>

  <ul class="service-list">
    <li><span class="band"></span>Boiler replacements (free quote)</li>
    <li><span class="band"></span>General plumbing &amp; heating</li>
    <li><span class="band"></span>Tap replacements</li>
    <li><span class="band"></span>1st &amp; 2nd fix</li>
    <li><span class="band"></span>New builds &amp; Extensions</li>
    <li><span class="band"></span>Cylinder replcemets</li>
  </ul>

  <div class="call">
    <svg class="call-icon" width="88" height="90" viewBox="0 0 88 90" aria-hidden="true">
      <path d="M20 4 L32 16 L20 30 C26 46 40 60 56 66 L70 54 L84 66 L68 84 C38 82 6 52 4 22 Z"
        fill="var(--orange)" stroke="var(--white)" stroke-width="4" stroke-linejoin="round"/>
    </svg>
    <div class="call-title">GIVE US A CALL</div>
    <div class="call-number">01632 870512</div>
  </div>

  <ul class="contacts">
    <li>
      <svg width="25" height="36" viewBox="0 0 25 36" aria-hidden="true"><path d="M12.5 0 C16 8 25 15 25 23 A12.5 12.5 0 0 1 0 23 C0 15 9 8 12.5 0Z" fill="var(--white)"/><rect x="8" y="15" width="9" height="15" rx="1.5" fill="var(--orange)"/><rect x="9.5" y="17" width="6" height="9" fill="var(--white)"/></svg>
      07700 914226
    </li>
    <li>
      <svg width="25" height="36" viewBox="0 0 25 36" aria-hidden="true"><path d="M12.5 0 C16 8 25 15 25 23 A12.5 12.5 0 0 1 0 23 C0 15 9 8 12.5 0Z" fill="var(--white)"/><rect x="5" y="17" width="15" height="11" rx="1.5" fill="var(--orange)"/><path d="M5.5 18 L12.5 23.5 L19.5 18" fill="none" stroke="var(--blue-deep)" stroke-width="1.2"/></svg>
      Info@brackenfoldplumbing.example.co.uk
    </li>
    <li>
      <svg width="25" height="36" viewBox="0 0 25 36" aria-hidden="true"><path d="M12.5 0 C16 8 25 15 25 23 A12.5 12.5 0 0 1 0 23 C0 15 9 8 12.5 0Z" fill="var(--white)"/><circle cx="12.5" cy="23" r="8" fill="var(--orange)" stroke="var(--blue-deep)" stroke-width="1.2"/><path d="M4.5 23 H20.5 M12.5 15 V31" fill="none" stroke="var(--blue-deep)" stroke-width="1.2"/></svg>
      www.brackenfold-plumbing.example.co.uk
    </li>
  </ul>

  <div class="social">
    <span><i></i>Chatterly</span>
    <span><i></i>pixgram</span>
  </div>

  <div class="footer-name">Brackenfold Plumbing Solutions</div>
</div>
</body>
</html>
```